The most modern business card ever !!!

Our company call “Vantilo”. Vantilo is a technology company specialized in cruises solutions. Out main product is a platform to reserve cruises. This is a revolutionary platform that make easier to travel agencies and final users to reserve cruises across dozen companies like tarvik, welbi, dpv, hbt, etc..We are a “start up”, with a young team of developers and we want to transmit it.. For it, we want something different, a modern business card that represent cruises and technology.. When someone receive this card, this person should say: wowww this is different… this is modern… this is a cruise related company..
Contact Information for Business Card
Requirements
Must have
- diferent, modern
Should not have
- traditions business card

```html
<!DOCTYPE html>
<html lang="en">
<head>
<meta charset="utf-8">
<title>Vantilo Business Card</title>
<link rel="stylesheet" href="https://fonts.googleapis.com/css2?family=Tenor+Sans&display=swap">
<style>
  :root {
    --ink: #000000;
    --card-grey: #808080;
    --paper: #ffffff;
    --text-dark: #0a0a0a;
  }
  html, body {
    margin: 0;
    padding: 0;
    width: 1200px;
    height: 686px;
    overflow: hidden;
    background: var(--paper);
  }
  .card {
    position: relative;
    width: 1200px;
    height: 686px;
    background: var(--card-grey);
    box-sizing: border-box;
    border: 11px solid var(--ink);
    overflow: hidden;
    font-family: "Tenor Sans", "Gill Sans", sans-serif;
    font-variant: small-caps;
    color: var(--text-dark);
  }
  .card__emblem {
    position: absolute;
    left: -11px;
    top: -11px;
    width: 1200px;
    height: 686px;
  }
  .contact {
    position: absolute;
    left: 50px;
    top: 92px;
    width: 450px;
    text-align: center;
    line-height: 1;
  }
  .contact__name {
    margin: 0;
    font-size: 56px;
    font-weight: 400;
    letter-spacing: 2px;
  }
  .contact__title {
    margin: 4px 0 0;
    font-size: 26px;
    letter-spacing: 1.5px;
  }
  .contact__group {
    margin: 0;
    font-size: 26px;
    letter-spacing: 1.5px;
    line-height: 34px;
  }
  .contact__group--reach { margin-top: 48px; }
  .contact__group--address { margin-top: 34px; }
  .contact__group--social { margin-top: 34px; }
  .contact__phone { font-variant: normal; }
</style>
</head>
<body>
  <div class="card">
    <svg class="card__emblem" viewBox="0 0 1200 686" xmlns="http://www.w3.org/2000/svg" aria-hidden="false">
      <defs>
        <clipPath id="emblem-inner">
          <path d="M851 62 L1120 62 L1120 331 A269 269 0 0 1 851 600 A269 269 0 0 1 582 331 A269 269 0 0 1 851 62 Z"/>
        </clipPath>
        <linearGradient id="ship-tone" x1="0" y1="0" x2="1" y2="1">
          <stop offset="0" stop-color="#f4f4f4"/>
          <stop offset="1" stop-color="#c9c9c9"/>
        </linearGradient>
      </defs>
      <path class="emblem__outer" fill="var(--ink)"
            d="M851 -12 L1194 -12 L1194 331 A343 343 0 0 1 851 674 A343 343 0 0 1 508 331 A343 343 0 0 1 851 -12 Z"/>
      <path class="emblem__band" fill="var(--card-grey)"
            d="M851 17 L1165 17 L1165 331 A314 314 0 0 1 851 645 A314 314 0 0 1 537 331 A314 314 0 0 1 851 17 Z"/>
      <path class="emblem__inner" fill="var(--ink)"
            d="M851 62 L1120 62 L1120 331 A269 269 0 0 1 851 600 A269 269 0 0 1 582 331 A269 269 0 0 1 851 62 Z"/>
      <g clip-path="url(#emblem-inner)" role="img" aria-label="Cruise ship illustration seen bow-first">
        <rect x="640" y="200" width="430" height="280" rx="60" fill="url(#ship-tone)"/>
      </g>
    </svg>

    <div class="contact">
      <h1 class="contact__name">Your Name</h1>
      <p class="contact__title">Your Title</p>
      <p class="contact__group contact__group--reach">
        <span class="contact__phone">1 111-111-1111</span><br>
        yourwebsite.com<br>
        youremail@website.com
      </p>
      <p class="contact__group contact__group--address">
        111 Address<br>
        Building/Suite Number<br>
        City, State Zip Code
      </p>
      <p class="contact__group contact__group--social">Social Media Address</p>
    </div>
  </div>
</body>
</html>
```